Website Landing Page for Medical Recruitment

Looking for a landing page to add to our existing website. The objective of the page is to recruit new clinical staff for various departments within Larkfield Medical Center (non-profit hospital in the Richmond, TX area).

We would like the page to be modern, professional, and non-cluttered. Please include call-to-actions and include a button that will navigate to the page where candidates can submit their applications (this page already exists).

Target Market(s)

25-35-year-olds who live in the Houston and Richmond area with medical experience.

Industry/Entity Type

Medical/Health

Font styles to use
Sans Serif

Colors
0054AA
0677BA
7BADD7
CADEEF
E8F1F8

Requirements
Must have
• A "call to action"; a button that navigates to larkfieldmedhub.example/careers

```html
<!DOCTYPE html>
<html lang="en">
<head>
<meta charset="utf-8">
<title>Careers – Larkfield Medical Center</title>
<link href="https://fonts.googleapis.com/css2?family=Exo+2:wght@400;500;600;700&family=Open+Sans:wght@400;600;700&display=swap" rel="stylesheet">
<style>
:root{
  --blue:#0054AA;
  --blue-mid:#0677BA;
  --blue-soft:#7BADD7;
  --blue-pale:#CADEEF;
  --blue-mist:#E8F1F8;
  --teal:#1fb5d9;
  --teal-soft:#6ec6e6;
  --grey-tag:#6b6b6b;
  --text:#6a6a6a;
  --section-grey:#f7f7f8;
  --footer:#2c3a4b;
  --footer-text:#b9c2cd;
  --orange:#f39c12;
  --red:#e02424;
}
*{box-sizing:border-box;margin:0;padding:0}
html,body{width:1200px;height:3703px;overflow:hidden}
body{position:relative;background:#fff;font-family:"Open Sans",Arial,sans-serif;color:var(--text)}
a{text-decoration:none;color:inherit}
.abs{position:absolute}

/* top bar */
.topbar{top:0;left:0;width:1200px;height:40px;border-bottom:1px solid #eee;font-size:11px;color:#777;display:flex;align-items:center;padding:0 70px}
.topbar .item{display:flex;align-items:center;gap:5px;margin-right:16px;white-space:nowrap}
.topbar .item svg{width:11px;height:11px}
.topbar .social{margin-left:auto;display:flex;gap:9px}
.topbar .social span{width:16px;height:16px;background:#b8bec6;border-radius:3px}

/* nav */
.nav{top:40px;left:0;width:1200px;height:63px;display:flex;align-items:center;padding:0 70px;border-bottom:1px solid #eee}
.brand{display:flex;align-items:center;gap:8px;font-family:"Exo 2",sans-serif;font-weight:600;font-size:21px;color:var(--blue)}
.brand .dot{width:26px;height:26px;border-radius:50%;background:var(--blue)}
.menu{margin-left:auto;display:flex;gap:18px;font-family:"Exo 2",sans-serif;font-size:13.5px;color:#555;align-items:center}
.menu .active{color:var(--teal)}
.menu .alert{color:var(--red)}
.menu svg{width:15px;height:15px;margin-left:6px}

/* hero */
.hero{top:103px;left:0;width:1200px;height:325px;background:linear-gradient(100deg,#243d63 0%,#2f4c75 45%,#20375a 100%)}
.hero-title{left:70px;top:195px;font-family:"Exo 2",sans-serif;font-weight:400;font-size:38px;color:#fff;letter-spacing:1px}
.hero-sub{left:72px;top:255px;width:490px;font-family:"Exo 2",sans-serif;font-size:18.5px;line-height:25px;color:#fff}
.hero-portrait{left:645px;top:115px;width:330px;height:264px;border-radius:50% 50% 0 0;background:linear-gradient(160deg,#ffffff 0%,#dfe9f4 45%,#4c8fd1 100%)}

/* search */
.search{top:379px;left:139px;width:921px;height:133px;background:#fff;border-top:6px solid var(--teal);box-shadow:0 4px 14px rgba(0,0,0,.12)}
.search label{position:absolute;top:42px;font-size:12px;font-weight:600;color:#444}
.search .field{position:absolute;top:66px;height:48px;border:1px solid #e2e2e2;font-size:12px;color:#aaa;padding:14px 10px}
.search .find{position:absolute;top:66px;left:779px;width:114px;height:48px;background:var(--teal-soft);color:#fff;font-size:12px;font-weight:700;display:flex;align-items:center;justify-content:center;gap:6px}

/* welcome */
.welcome-art{left:237px;top:556px;width:338px;height:324px;border-radius:50% 10% 50% 50%;background:linear-gradient(135deg,#c9d8e8 0%,#9a7b63 55%,#6f8c4c 100%)}
.welcome-title{left:613px;top:636px;font-family:"Exo 2",sans-serif;font-weight:700;font-size:25px;color:#222;letter-spacing:.5px}
.welcome-text{left:614px;top:694px;width:420px;font-size:13.5px;line-height:25.5px;color:#555}
.welcome-text a{color:var(--blue);text-decoration:underline}

/* jobs */
.jobs{top:880px;left:0;width:1200px;height:1671px;background:var(--section-grey)}
.section-title{width:1200px;left:0;text-align:center;font-family:"Exo 2",sans-serif;font-weight:700;font-size:25px;color:#222}
.job{position:absolute;width:518px;height:344px;background:#fff;border:1px solid #e6e6e6;padding:38px 27px 0}
.job .loc{font-size:12px;color:#666}
.job h3{margin-top:12px;width:440px;font-family:"Exo 2",sans-serif;font-weight:400;font-size:18.5px;line-height:24.5px;color:var(--blue)}
.job p{margin-top:12px;width:445px;font-size:11.5px;line-height:22px;color:#666}
.job p.long{margin-top:10px;width:462px;font-size:11px;line-height:19.5px}
.tags{position:absolute;left:27px;bottom:37px;display:flex;gap:7px}
.tag{height:30px;display:flex;align-items:center;justify-content:center;color:#fff;font-size:11px;white-space:nowrap}
.tag.cat{width:203px;background:var(--blue)}
.tag.cat b{font-weight:700;margin-right:4px}
.tag.id{width:121px;background:var(--grey-tag)}
.tag.shift{width:120px;background:var(--blue-soft)}
.tag.shift.wide{width:135px}
.pager{top:2489px;left:0;width:1200px;display:flex;justify-content:center;gap:14px;font-size:11px;font-weight:700;color:#555;align-items:center}
.pager .on{width:19px;height:19px;border-radius:50%;background:#555;color:#fff;display:flex;align-items:center;justify-content:center}

/* testimonials */
.quote{position:absolute;top:2653px;width:334px;height:199px;background:#f4f4f4;border-radius:26px;padding:22px 16px}
.stars{display:flex;gap:2px}
.stars svg{width:13px;height:13px}
.quote p{margin-top:10px;font-family:Arial,sans-serif;font-size:12px;line-height:22px;color:#555}
.quote .more{position:absolute;top:114px;left:16px;font-size:12px;color:#777}
.quote .posted{position:absolute;top:150px;left:17px;font-size:10.5px;color:#888}
.quote .site{position:absolute;top:164px;left:17px;font-size:19px;font-weight:700;color:var(--blue-mid)}
.person{position:absolute;top:2877px;display:flex;align-items:center;gap:12px}
.person .av{width:40px;height:40px;border-radius:50%;color:#fff;font-weight:700;font-size:14px;display:flex;align-items:center;justify-content:center}
.person b{display:block;font-family:"Exo 2",sans-serif;font-size:12.5px;color:#222}
.person small{font-size:10.5px;color:#777}
.dots{top:2963px;left:575px;display:flex;gap:12px}
.dots span{width:8px;height:8px;border-radius:50%;background:#ddd}
.dots span.on{background:#777}

/* footer */
.footer{top:3054px;left:0;width:1200px;height:649px;background:var(--footer)}
.f-head{font-family:"Exo 2",sans-serif;font-weight:600;font-size:16px;color:#fff}
.feed{left:70px;top:3150px;width:317px;height:382px;background:#fff;overflow:hidden}
.feed .cover{height:116px;background:linear-gradient(180deg,#6b4a3c 0%,#8a6a55 60%,#3b4b5c 100%);position:relative}
.feed .cover .pg{position:absolute;left:12px;top:8px;width:32px;height:32px;background:#fff;border:1px solid #ccc}
.feed .cover .nm{position:absolute;left:50px;top:6px;font-family:Arial,sans-serif;font-size:16px;color:#fff}
.feed .cover .lk{position:absolute;left:50px;top:27px;font-family:Arial,sans-serif;font-size:10.5px;color:#fff}
.feed .btn{position:absolute;top:90px;height:20px;background:#f5f6f7;border:1px solid #ccc;font-family:Arial,sans-serif;font-size:10.5px;color:#4b4f56;padding:2px 8px}
.feed .post{padding:14px 18px 0;font-family:Arial,sans-serif}
.feed .post .who{display:flex;gap:8px;align-items:center}
.feed .post .who span{width:34px;height:34px;border-radius:50%;background:var(--blue-mid)}
.feed .post .who b{font-size:12.5px;color:#1d2129;font-weight:700}
.feed .post .who small{display:block;font-size:10px;color:#90949c}
.feed .post p{margin-top:14px;font-size:12.5px;line-height:17px;color:#1d2129}
.feed .shot{position:absolute;left:18px;top:282px;width:281px;height:100px;background:linear-gradient(90deg,#c9b8a6 0%,#8f7a66 50%,#b7a896 100%)}
.contact{left:790px;top:3142px;width:220px;font-family:"Exo 2",sans-serif;font-size:13px;line-height:29px;color:var(--footer-text);white-space:nowrap}
.contact .ln{display:flex;align-items:center;gap:9px;color:#8b96a3;font-size:12.5px}
.contact .ln svg{width:12px;height:12px;flex:none}
.map-btn{left:790px;top:3398px;width:171px;height:46px;background:var(--teal);color:#fff;font-family:"Exo 2",sans-serif;font-weight:600;font-size:14px;display:flex;align-items:center;justify-content:center;gap:6px}
.access-icon{left:812px;top:3456px;width:62px;height:50px;border-radius:40% 50% 45% 40%;background:#151a21}
.donate{left:1025px;top:3320px;width:175px;height:44px;background:var(--blue);color:#fff;font-family:"Exo 2",sans-serif;font-weight:700;font-size:18px;display:flex;align-items:center;justify-content:center;gap:6px;border-radius:4px 0 0 4px}
.copy{top:3610px;left:0;width:1200px;text-align:center;font-size:12px;color:#c8d0d9}
.copy b{color:#fff;font-weight:600}
.cards{top:3643px;left:480px;display:flex;gap:5px}
.cards span{width:57px;height:37px;border-radius:3px;border:2px solid #fff}
.to-top{left:1161px;top:3650px;width:39px;height:39px;background:var(--teal);display:flex;align-items:center;justify-content:center}
</style>
</head>
<body>

<div class="abs topbar">
  <span class="item"><svg viewBox="0 0 12 12"><path d="M6 1a3.5 3.5 0 0 0-3.5 3.5C2.5 7.5 6 11 6 11s3.5-3.5 3.5-6.5A3.5 3.5 0 0 0 6 1zm0 5a1.4 1.4 0 1 1 0-2.8A1.4 1.4 0 0 1 6 6z" fill="#1fb5d9"/></svg>2240 Meadowline Avenue, Richmond, Texas</span>
  <span class="item"><svg viewBox="0 0 12 12"><rect x="3.5" y="1" width="5" height="10" rx="1" fill="none" stroke="#1fb5d9" stroke-width="1.2"/></svg>Call: 281-555-0142</span>
  <span class="item">Careers</span>
  <span class="item">Physician/Staff Login</span>
  <span class="item">Patient Portal</span>
  <span class="item">Pay My Bill</span>
  <span class="item">Contact Us ▾</span>
  <span class="item">Larkfield Medical Group ▾</span>
  <span class="social"><span></span><span></span><span></span><span></span></span>
</div>

<div class="abs nav">
  <div class="brand"><span class="dot"></span>Larkfield</div>
  <nav class="menu">
    <a class="active">Home</a><a>Find A Doctor</a><a class="alert">COVID-19</a><a>About Us</a><a>Services</a><a>Locations</a><a>Patients/Visitors</a><a>Ways To Give</a><a>Health Library</a>
    <svg viewBox="0 0 16 16"><circle cx="7" cy="7" r="5" fill="none" stroke="#555" stroke-width="2"/><path d="M11 11l4 4" stroke="#555" stroke-width="2"/></svg>
  </nav>
</div>

<div class="abs hero" role="img" aria-label="Photo of the hospital building in dark blue tone"></div>
<div class="abs hero-portrait" role="img" aria-label="Photo of a smiling nurse in blue scrubs holding a clipboard"></div>
<h1 class="abs hero-title">Careers</h1>
<p class="abs hero-sub">We’re hiring for multiple nursing position in a variety of our department</p>

<form class="abs search">
  <label style="left:29px">Search Topic</label>
  <label style="left:413px">Category</label>
  <label style="left:601px">Location</label>
  <div class="field" style="left:29px;width:380px">Search clinic,hospitals etc</div>
  <div class="field" style="left:411px;width:184px">(All)</div>
  <div class="field" style="left:596px;width:184px">(All)</div>
  <a class="find" href="https://larkfieldmedhub.example/careers"><svg width="12" height="12" viewBox="0 0 16 16"><circle cx="7" cy="7" r="5" fill="none" stroke="#fff" stroke-width="2"/><path d="M11 11l4 4" stroke="#fff" stroke-width="2"/></svg>Find Now</a>
</form>

<div class="abs welcome-art" role="img" aria-label="Leaf-shaped photo of the Larkfield Medical Center building"></div>
<h2 class="abs welcome-title">Welcome</h2>
<p class="abs welcome-text">Welcome to our employment section. Here you can view our current job openings and&nbsp; apply for positions online. Or, if you prefer, you can simply <a href="https://larkfieldmedhub.example/careers">submit your resume</a> for general consideration.</p>

<section class="abs jobs"></section>
<h2 class="abs section-title" style="top:920px">Latest Jobs</h2>

<article class="job" style="left:70px;top:987px">
  <div class="loc">US-TX-Richmond</div>
  <h3>Registered Nurse - ICU - Full Time Days (7a-7p) - $15,000 Sign On Bonus</h3>
  <p>$15,000 Bonus - Certain criteria is required to qualify for the bonus.&nbsp;&nbsp; The Registered Nurse is responsible for professional nursing care and related assistance to patients in the ICU. The staff nurse provides direction to non-licensed assertive personnel in providing direct patient care. The staff nurse supports the medical care of patients under the direction of the Medical Staff pursuant to the objectives of the hospital.</p>
  <div class="tags"><span class="tag cat"><b>Category</b> - Nursing</span><span class="tag id">ID&nbsp; 2022-3016</span><span class="tag shift">Shift&nbsp; Days</span></div>
</article>
<article class="job" style="left:611px;top:987px">
  <div class="loc">US-TX-Wharton</div>
  <h3>Registered Nurse - ECC Wharton - Full Time - Days - $15,000 Sign-On Bonus</h3>
  <p>The Registered Nurse at Wharton Campus is responsible for professional nursing care and related assistance to patients on an assigned unit.&nbsp; The staff nurse provides direction to licensed vocational nurses and non-professional nursing personnel in providing direct patient care.&nbsp; The staff nurse supports the medical care of patients under the direction of the Medical Staff pursuant to the objectives of the hospital.</p>
  <div class="tags"><span class="tag cat"><b>Category</b> - Nursing</span><span class="tag id">ID&nbsp; 2022-3013</span><span class="tag shift">Shift&nbsp; 7a-7p</span></div>
</article>

<article class="job" style="left:70px;top:1365px">
  <div class="loc">US-TX-Richmond</div>
  <h3>Registered Nurse - ICU - PRN<br>(Internal Applicants Only)</h3>
  <p>The Registered Nurse is responsible for professional nursing care and related assistance to patients in the ICU. The staff nurse provides direction to non-licensed assertive personnel in providing direct patient care. The staff nurse supports the medical care of patients under the direction of the Medical Staff pursuant to the objectives of the hospital.</p>
  <div class="tags"><span class="tag cat"><b>Category</b> - Nursing</span><span class="tag id">ID&nbsp; 2022-3016</span><span class="tag shift">Shift&nbsp;&nbsp; 7a-7p</span></div>
</article>
<article class="job" style="left:611px;top:1365px">
  <div class="loc">US-TX-Richmond</div>
  <h3>Registered Nurse - ICU - Full Time - Days<br>(Internal Applicants Only)</h3>
  <p>The Registered Nurse is responsible for professional nursing care and related assistance to patients in the ICU. The staff nurse provides direction to non-licensed assertive personnel in providing direct patient care. The staff nurse supports the medical care of patients under the direction of the Medical Staff pursuant to the objectives of the hospital.</p>
  <div class="tags"><span class="tag cat"><b>Category</b> - Nursing</span><span class="tag id">ID&nbsp; 2022-3013</span><span class="tag shift">Shift&nbsp; 7a</span></div>
</article>

<article class="job" style="left:70px;top:1736px">
  <div class="loc">US-TX-Richmond</div>
  <h3>Security Officer - Full Time - Nights</h3>
  <p>Under the general direction of the Security Manager, the Security Officer is responsible for the general work in the protection of persons and property, and the enforcement of all applicable policies, rules, and regulations at Larkfield Medical Center. Observes behavioral health patients as assigned. Also to include applicable federal, state, and local laws to prevent losses due to accidents and incidents.</p>
  <div class="tags"><span class="tag cat"><b>Category</b> - Nursing</span><span class="tag id">ID&nbsp; 2022-3016</span><span class="tag shift wide">Shift&nbsp; 10:30pm - 7:00am</span></div>
</article>
<article class="job" style="left:611px;top:1736px">
  <div class="loc">US-TX-Richmond</div>
  <h3>Housekeeper I</h3>
  <p>Under the direct supervison of the Building Services Supervisor, the Housekeeper I is responsible for the disinfection and general cleaning of patient care areas, treatment rooms, and other areas of the facility in accordance with established standards.</p>
  <div class="tags"><span class="tag cat"><b>Category</b> - Building Services</span><span class="tag id">ID&nbsp; 2022-3013</span><span class="tag shift">Shift&nbsp; 7a</span></div>
</article>

<article class="job" style="left:70px;top:2105px">
  <div class="loc">US-TX-Richmond</div>
  <h3>Registered Nurse - ECC (MA/WH) - Full Time (1p-1a) - $15,000 Sign-On Bonus</h3>
  <p>Under the general direction of the Security Manager, the Security Officer is responsible for the general work in the protection of persons and property, and the enforcement of all applicable policies, rules, and regulations at Larkfield Medical Center. Observes behavioral health patients as assigned. Also to include applicable federal, state, and local laws to prevent losses due to accidents and incidents.</p>
  <div class="tags"><span class="tag cat"><b>Category</b> - Nursing</span><span class="tag id">ID&nbsp; 2022-3016</span><span class="tag shift wide">Shift&nbsp; 10:30pm - 7:00am</span></div>
</article>
<article class="job" style="left:611px;top:2105px">
  <div class="loc">US-TX-Richmond</div>
  <h3>Lead Emergency Room Technician - ECC - Full Time - Nights</h3>
  <p class="long">Under the general supervision of the Clinical Coordinator (RN), the Lead Emergency Room Technician (Lead ERT) is responsible for the supervision and training of ERTs to ensure the administration of excellent patient care and customer service, EKG monitoring, and assist licensed nursing staff to provide care to Emergency Care Center patients.&nbsp; The Lead ERT will continue to support the medical care of patients under the direction of the Medical Staff pursuant to the objectives of the hospital.</p>
  <div class="tags"><span class="tag cat"><b>Category</b> - Building Services</span><span class="tag id">ID&nbsp; 2022-3013</span><span class="tag shift">Shift&nbsp; 7a</span></div>
</article>

<div class="abs pager"><span class="on">1.</span><span>2.</span><span>3.</span><span>4.</span><span>5</span></div>

<h2 class="abs section-title" style="top:2596px">Client Testimonial</h2>

<div class="quote" style="left:75px">
  <div class="stars"><svg viewBox="0 0 10 10"><path d="M5 .5l1.4 2.9 3.1.4-2.3 2.2.6 3.1L5 7.6 2.2 9.1l.6-3.1L.5 3.8l3.1-.4z" fill="#f39c12"/></svg><svg viewBox="0 0 10 10"><path d="M5 .5l1.4 2.9 3.1.4-2.3 2.2.6 3.1L5 7.6 2.2 9.1l.6-3.1L.5 3.8l3.1-.4z" fill="#f39c12"/></svg><svg viewBox="0 0 10 10"><path d="M5 .5l1.4 2.9 3.1.4-2.3 2.2.6 3.1L5 7.6 2.2 9.1l.6-3.1L.5 3.8l3.1-.4z" fill="#f39c12"/></svg><svg viewBox="0 0 10 10"><path d="M5 .5l1.4 2.9 3.1.4-2.3 2.2.6 3.1L5 7.6 2.2 9.1l.6-3.1L.5 3.8l3.1-.4z" fill="#f39c12"/></svg><svg viewBox="0 0 10 10"><path d="M5 .5l1.4 2.9 3.1.4-2.3 2.2.6 3.1L5 7.6 2.2 9.1l.6-3.1L.5 3.8l3.1-.4z" fill="#f39c12"/></svg></div>
  <p>they were very nice and all was well until I waited almost 2 hours to get discharged!</p>
  <span class="more">Read More</span><span class="posted">Posted on</span><span class="site">Rateboard</span>
</div>
<div class="quote" style="left:434px">
  <div class="stars"><svg viewBox="0 0 10 10"><path d="M5 .5l1.4 2.9 3.1.4-2.3 2.2.6 3.1L5 7.6 2.2 9.1l.6-3.1L.5 3.8l3.1-.4z" fill="#f39c12"/></svg><svg viewBox="0 0 10 10"><path d="M5 .5l1.4 2.9 3.1.4-2.3 2.2.6 3.1L5 7.6 2.2 9.1l.6-3.1L.5 3.8l3.1-.4z" fill="#f39c12"/></svg><svg viewBox="0 0 10 10"><path d="M5 .5l1.4 2.9 3.1.4-2.3 2.2.6 3.1L5 7.6 2.2 9.1l.6-3.1L.5 3.8l3.1-.4z" fill="#f39c12"/></svg><svg viewBox="0 0 10 10"><path d="M5 .5l1.4 2.9 3.1.4-2.3 2.2.6 3.1L5 7.6 2.2 9.1l.6-3.1L.5 3.8l3.1-.4z" fill="#f39c12"/></svg><svg viewBox="0 0 10 10"><path d="M5 .5l1.4 2.9 3.1.4-2.3 2.2.6 3.1L5 7.6 2.2 9.1l.6-3.1L.5 3.8l3.1-.4z" fill="#f39c12"/></svg></div>
  <p>The staff as well as there services and time and clean facility.</p>
  <span class="more">Read More</span><span class="posted">Posted on</span><span class="site">Rateboard</span>
</div>
<div class="quote" style="left:793px">
  <div class="stars"><svg viewBox="0 0 10 10"><path d="M5 .5l1.4 2.9 3.1.4-2.3 2.2.6 3.1L5 7.6 2.2 9.1l.6-3.1L.5 3.8l3.1-.4z" fill="#f39c12"/></svg><svg viewBox="0 0 10 10"><path d="M5 .5l1.4 2.9 3.1.4-2.3 2.2.6 3.1L5 7.6 2.2 9.1l.6-3.1L.5 3.8l3.1-.4z" fill="#f39c12"/></svg><svg viewBox="0 0 10 10"><path d="M5 .5l1.4 2.9 3.1.4-2.3 2.2.6 3.1L5 7.6 2.2 9.1l.6-3.1L.5 3.8l3.1-.4z" fill="#f39c12"/></svg><svg viewBox="0 0 10 10"><path d="M5 .5l1.4 2.9 3.1.4-2.3 2.2.6 3.1L5 7.6 2.2 9.1l.6-3.1L.5 3.8l3.1-.4z" fill="#f39c12"/></svg><svg viewBox="0 0 10 10"><path d="M5 .5l1.4 2.9 3.1.4-2.3 2.2.6 3.1L5 7.6 2.2 9.1l.6-3.1L.5 3.8l3.1-.4z" fill="#f39c12"/></svg></div>
  <p>The staff as well as there services and time and clean facility.</p>
  <span class="more">Read More</span><span class="posted">Posted on</span><span class="site">Rateboard</span>
</div>

<div class="person" style="left:112px"><span class="av" style="background:#5d3b30">M</span><div><b>Marisol Grant</b><small>9 days ago</small></div></div>
<div class="person" style="left:470px"><span class="av" style="background:#d9532f">T</span><div><b>Tessa Whitford</b><small>9 days ago</small></div></div>
<div class="person" style="left:829px"><span class="av" style="background:#2aa3a8">R</span><div><b>Renata Alvarez</b><small>9 days ago</small></div></div>
<div class="abs dots"><span class="on"></span><span></span><span></span></div>

<footer class="abs footer"></footer>
<h4 class="abs f-head" style="left:70px;top:3104px">Community Feed</h4>
<div class="abs feed">
  <div class="cover" role="img" aria-label="Cover photo of the hospital exterior">
    <span class="pg"></span>
    <span class="nm">Larkfield Medical Center</span>
    <span class="lk">9,829 likes</span>
  </div>
  <span class="btn" style="left:10px">Like Page</span>
  <span class="btn" style="left:224px">Contact us</span>
  <div class="post">
    <div class="who"><span></span><div><b>Larkfield Medical Center</b><small>on Wednesday</small></div></div>
    <p>Our Marketing Team has been working with Brightlane Productions on producing a series of short video ads. We just wrapped up Day 2 of video production and can't wait to see the finished product. Stay tuned for updates!</p>
  </div>
  <div class="shot" role="img" aria-label="Photo from the video shoot inside the hospital"></div>
</div>

<h4 class="abs f-head" style="left:790px;top:3104px">Contact Details</h4>
<div class="abs contact">
  <div>Larkfield Medical Center</div>
  <div>Meadowline Hospital Campus</div>
  <div>2240 Meadowline Avenue, Richmond</div>
  <div>Texas 77406</div>
  <div class="ln"><svg viewBox="0 0 12 12"><path d="M2.5 1h2l1 2.5-1.3 1a6 6 0 0 0 3.3 3.3l1-1.3L11 7.5v2A1.5 1.5 0 0 1 9.5 11 8.5 8.5 0 0 1 1 2.5 1.5 1.5 0 0 1 2.5 1z" fill="#1fb5d9"/></svg>281-555-0142</div>
  <div class="ln"><svg viewBox="0 0 12 12"><rect x="1" y="2.5" width="10" height="7" fill="none" stroke="#1fb5d9" stroke-width="1.2"/><path d="M1 2.5l5 4 5-4" fill="none" stroke="#1fb5d9" stroke-width="1.2"/></svg>info@larkfieldmc.example</div>
  <div class="ln"><svg viewBox="0 0 12 12"><rect x="1" y="2.5" width="10" height="7" fill="none" stroke="#1fb5d9" stroke-width="1.2"/><path d="M1 2.5l5 4 5-4" fill="none" stroke="#1fb5d9" stroke-width="1.2"/></svg>jobs@larkfieldmc.example</div>
  <div class="ln"><svg viewBox="0 0 12 12"><circle cx="6" cy="6" r="5" fill="#1fb5d9"/></svg>www.larkfieldmc.example</div>
</div>
<a class="abs map-btn" href="https://larkfieldmedhub.example/careers">Get Map Direction <svg width="16" height="10" viewBox="0 0 16 10"><path d="M0 5h13M9 1l4 4-4 4" fill="none" stroke="#fff" stroke-width="2"/></svg></a>
<div class="abs access-icon" role="img" aria-label="Sign language interpreting accessibility icon"></div>
<a class="abs donate" href="https://larkfieldmedhub.example/careers"><span style="font-size:24px">$</span> DONATE NOW</a>

<p class="abs copy">Copyright Larkfield 2022-23 | Proudly Powered By <b>Northgate Web Studio LLC</b> | <b>Privacy Policy</b> | <b>Refund Policy</b> | <b>Public Information Request</b></p>
<div class="abs cards"><span style="background:#e8e8e8"></span><span style="background:#f2f2f2"></span><span style="background:#dfe6f3"></span><span style="background:#4f8fd6"></span></div>
<a class="abs to-top" href="#"><svg width="14" height="10" viewBox="0 0 14 10"><path d="M1 8l6-6 6 6" fill="none" stroke="#fff" stroke-width="2"/></svg></a>

</body>
</html>
```